Business Card Needed for Crafter of Pottery, Jewelry and Artwork

Calling all designers in search of an artistic challenge.

I need a new business card design for my pottery, jewelry and artwork business, Woven Glass and Tide, based in Vancouver BC.

I would like a card that is bright and inviting and preferably incorporates my logo and a sample of photos of my work while having a clean fresh look. The following contact details would preferably be included on the card as well:
• Helena Pikeworth
• Designer
• Phone: 604.555.0172
• Email: Designer@WovenGlassandTide.example
• Website: www.WovenGlassandTide.example
• Blog: www.ShapingHillside.example

The logo is attached in two color schemes in both Vector and Source formats. On past cards I’ve also included photos of my work. By including photos of the work the pieces are showcased and it catches people’s eye and prompts them to pick up the card and look at it more closely. For example, if I leave a stack in a coffee shop I want people to be drawn to the card, to pick it up and get a sense of the my product lines. Please feel free to pull photos of my work directly off of my website. If you need photos with higher pixels please let me know and I’ll email them directly to you. The website background is bffbda (191, 251, 218). I would like the business cards to match the feel of the website for consistency but the cards do not need to use the exact same colors. My website and current business card are predominantly turquoise shades. The background uses stripes provided by the website template. I don’t know the exact colors of the stripes.

My current business card is attached to show the use of photos in a design. Please note that I am not thrilled with my own design and am looking for variations and completely new designs. This example is not meant to be used as a template or starting point.

Here is some background surrounding my company:
WGT offers one of a kind jewelry, pottery, artwork and leather bags each designed with a twist. The pottery varies from rustic every day functional ware to raku artwork. The jewelry ranges from simple sterling every day pieces to multimedia pieces incorporating stone, metal, ceramics and fabric. The artwork is multimedia, typically acrylic paired with a natural element such as bark. All the bags are leather with reworked kimono fabric or patterned silk lining.

Feel free to check out my website to get a flavour for my work and the color scheme I've used on marketing materials so far. www.wovenglassandtide.example
Updates

Thank you to everyone who has submitted a design so far. I hope everyone has received some helpful feedback.

I'm going to post a survey to customers and friends asking for their votes. If you have new designs to submit please try to get them in by Saturday March 30 at noon so that I can include it in the survey launch.

Thank you

Target Market(s)

Females aged 25-65 interested in one of a kind functional pottery and jewelry.

Industry/Entity Type

Coffee Shop

Requirements
Must have
• Contact information, website, blog
Nice to have
• Logo, photos

```html
<!DOCTYPE html>
<html lang="en">
<head>
<meta charset="utf-8">
<title>Woven Glass and Tide — Business Card</title>
<link rel="stylesheet" href="https://fonts.googleapis.com/css2?family=EB+Garamond:wght@400;500;700&display=swap">
<style>
  :root {
    --mint: #c6f6e0;
    --navy: #24225f;
    --teal: #3cbfb8;
    --teal-light: #8fe0d4;
    --ink: #1f1f1f;
    --stage: #ece8e2;
    --frame: #111111;
    --font-serif: "EB Garamond", Georgia, serif;
  }
  * { box-sizing: border-box; margin: 0; padding: 0; }
  html, body {
    width: 1200px; height: 379px; overflow: hidden;
    background: var(--stage);
    font-family: var(--font-serif);
    color: var(--ink);
  }
  .stage { position: relative; width: 1200px; height: 379px; }

  .card {
    position: absolute; top: 30px; width: 559px; height: 322px;
    background: var(--mint); overflow: hidden;
  }
  .card--front { left: 27px; }
  .card--back { left: 615px; }

  /* Front */
  .brand-mark {
    position: absolute; left: 28px; top: 15px; width: 182px; height: 182px;
    border: 2px solid var(--teal); border-radius: 50%;
    display: flex; align-items: center; justify-content: center; text-align: center;
  }
  .brand-mark__name {
    font-size: 24px; font-weight: 500; line-height: 1.05;
    color: var(--navy); letter-spacing: 0.04em; text-transform: uppercase;
    width: 140px;
  }
  .contact-list {
    position: absolute; left: 272px; top: 108px; list-style: none;
    font-size: 15px; line-height: 22.5px;
  }
  .contact-list li { display: flex; align-items: center; gap: 7px; }
  .contact-list svg { width: 12px; height: 12px; flex: none; }
  .icon-blog { width: 12px; height: 12px; background: #f26c21; border-radius: 2px; flex: none; }

  .wave { position: absolute; left: 0; bottom: 0; width: 559px; height: 80px; }
  .signature {
    position: absolute; left: 60px; top: 266px; width: 175px; text-align: center;
    color: #ffffff;
  }
  .signature__name { font-size: 20px; font-weight: 700; line-height: 1.1; }
  .signature__role { font-size: 15px; line-height: 1.3; }

  /* Back */
  .back-title {
    position: absolute; top: 6px; left: 0; width: 100%; text-align: center;
    font-size: 19px; letter-spacing: 0.28em; color: var(--navy); font-weight: 500;
  }
  .gallery {
    position: absolute; left: 15px; top: 38px;
    display: grid; grid-template-columns: repeat(3, 170px); grid-template-rows: repeat(2, 114px);
    column-gap: 13px; row-gap: 11px;
  }
  .gallery__item {
    border: 2px solid var(--frame); border-radius: 16px; overflow: hidden;
  }
  .gallery__item--mugs { background: linear-gradient(135deg, #e9ecea 0%, #9fc3c4 50%, #4a4d55 100%); }
  .gallery__item--necklace { background: radial-gradient(circle at 50% 55%, #c77a5a 0%, #d9b3a4 45%, #ece7e2 100%); }
  .gallery__item--pot { background: radial-gradient(circle at 50% 50%, #2f5fae 0%, #2a4c8e 45%, #e8e6e2 80%); }
  .gallery__item--plate { background: radial-gradient(circle at 50% 60%, #9fcab3 0%, #6fa78d 40%, #a38464 70%, #ebe6df 100%); }
  .gallery__item--bag { background: linear-gradient(180deg, #ecebe8 0%, #d8564b 30%, #c6463d 80%, #2a2a2a 100%); }
  .gallery__item--earrings { background: linear-gradient(135deg, #6b4d3a 0%, #b68b70 40%, #e46a8e 65%, #a9d6c2 100%); }
  .back-url {
    position: absolute; bottom: 14px; left: 0; width: 100%; text-align: center;
    font-size: 14px; letter-spacing: 0.14em; color: var(--ink);
  }
</style>
</head>
<body>
<main class="stage">
  <section class="card card--front" aria-label="Business card front">
    <div class="brand-mark">
      <span class="brand-mark__name">Woven Glass and Tide</span>
    </div>

    <ul class="contact-list">
      <li>
        <svg viewBox="0 0 12 12" aria-hidden="true"><path d="M3 1 L5 3.5 L3.8 5 Q5 7.3 7 8.2 L8.5 7 L11 9 L9.6 11 Q4.5 10.5 1 3 Z" fill="#222"/></svg>
        604.555.0172
      </li>
      <li>
        <svg viewBox="0 0 12 12" aria-hidden="true"><circle cx="6" cy="6" r="6" fill="#222"/><rect x="2.6" y="3.8" width="6.8" height="4.6" fill="#fff"/><path d="M2.6 3.8 L6 6.5 L9.4 3.8" stroke="#222" stroke-width="0.8" fill="none"/></svg>
        Designer@WovenGlassandTide.example
      </li>
      <li>
        <svg viewBox="0 0 12 12" aria-hidden="true"><circle cx="6" cy="6" r="5.3" fill="none" stroke="#222" stroke-width="1.2"/><ellipse cx="6" cy="6" rx="2.3" ry="5.3" fill="none" stroke="#222" stroke-width="1"/><path d="M0.7 6 H11.3" stroke="#222" stroke-width="1"/></svg>
        www.WovenGlassandTide.example
      </li>
      <li>
        <span class="icon-blog" aria-hidden="true"></span>
        www.ShapingHillside.example
      </li>
    </ul>

    <svg class="wave" viewBox="0 0 559 80" preserveAspectRatio="none" aria-hidden="true">
      <path d="M0 22 Q160 -6 300 18 Q430 40 559 60 L559 80 L0 80 Z" fill="var(--teal-light)"/>
      <path d="M0 26 Q160 2 300 24 Q430 45 559 66 L559 80 L0 80 Z" fill="var(--teal)"/>
      <path d="M0 34 Q170 12 310 34 Q440 54 559 72 L559 80 L0 80 Z" fill="var(--navy)"/>
    </svg>
    <div class="signature">
      <p class="signature__name">Helena Pikeworth</p>
      <p class="signature__role">Designer</p>
    </div>
  </section>

  <section class="card card--back" aria-label="Business card back">
    <h1 class="back-title">WOVEN GLASS AND TIDE</h1>
    <div class="gallery">
      <div class="gallery__item gallery__item--mugs" role="img" aria-label="Photo of teal and charcoal glazed pottery mugs"></div>
      <div class="gallery__item gallery__item--necklace" role="img" aria-label="Photo of a pink stone bead necklace with wooden pendant"></div>
      <div class="gallery__item gallery__item--pot" role="img" aria-label="Photo of a speckled blue lidded pottery jar"></div>
      <div class="gallery__item gallery__item--plate" role="img" aria-label="Photo of a pierced green glazed ceramic bowl"></div>
      <div class="gallery__item gallery__item--bag" role="img" aria-label="Photo of a red and black leather tote bag"></div>
      <div class="gallery__item gallery__item--earrings" role="img" aria-label="Photo of pink and seafoam beaded earrings on driftwood"></div>
    </div>
    <p class="back-url">www.WovenGlassandTide.example</p>
  </section>
</main>
</body>
</html>
```